Product Description Graphic

We are designing a new product and need a better graphic to describe it.

We are not worried about names of the modules yet but want to be descriptive of capabilities. Right now "Present & CMA" should really be "Presentations & CMA".

I overall like the shape of the triangle and the arrow for Contacts but this is a very unsophisticated graphic done by a non-designer. Also need to better show that each block of capabilites will also have paywall capabilities.

Target Market(s)

Real Estate Brokerage Firms and Real Estate Agents

Industry/Entity Type

Real Estate

Colors

Designer to choose colors to be used in the design.

Requirements
Must have
• Sophisticated design. Paywall description embedded.

```html
<!DOCTYPE html>
<html lang="en">
<head>
<meta charset="utf-8">
<title>Product Capabilities Pyramid</title>
<link href="https://fonts.googleapis.com/css2?family=Encode+Sans+Semi+Condensed:wght@600&family=Open+Sans:wght@400&display=swap" rel="stylesheet">
<style>
  :root {
    --bg-light: #ffffff;
    --bg-dark: #d2d2d2;
    --blue: #1f6a96;
    --blue-paywall: #4a88ad;
    --gold: #b68239;
    --gold-paywall: #c49c61;
    --navy: #273a5b;
    --navy-paywall: #505f7c;
    --coral: #cd675e;
    --coral-paywall: #d9867f;
    --teal: #3f6868;
    --teal-paywall: #688987;
    --label: #ffffff;
    --legend-swatch: #a7a7a7;
    --legend-body: #555555;
  }
  html, body {
    margin: 0;
    padding: 0;
    overflow: hidden;
  }
  .canvas {
    position: relative;
    width: 1200px;
    height: 1000px;
    overflow: hidden;
    background: radial-gradient(ellipse 95% 110% at 25% 20%, var(--bg-light) 35%, var(--bg-dark) 100%);
  }
  .pyramid {
    position: absolute;
    inset: 0;
    width: 1200px;
    height: 1000px;
  }
  .block {
    filter: drop-shadow(7px 9px 5px rgba(0, 0, 0, 0.3));
  }
  .icon {
    fill: none;
    stroke: var(--label);
    stroke-width: 1.6;
    stroke-linecap: round;
    stroke-linejoin: round;
  }
  .icon .solid { fill: var(--label); stroke: none; }
  .module-label {
    position: absolute;
    margin: 0;
    font-family: "Encode Sans Semi Condensed", "Arial Narrow", sans-serif;
    font-weight: 600;
    font-size: 19.5px;
    line-height: 23px;
    color: var(--label);
    text-align: center;
    letter-spacing: 0.2px;
    white-space: nowrap;
  }
  .label-email { left: 340px; top: 450px; width: 200px; }
  .label-presentations { left: 703px; top: 520px; width: 200px; }
  .label-contacts { left: 500px; top: 638px; width: 200px; }
  .label-websites { left: 274px; top: 785px; text-align: left; }
  .label-mobile { left: 858px; top: 785px; width: 100px; }
  .legend {
    position: absolute;
    left: 944px;
    top: 914px;
    width: 167px;
    height: 42px;
    border-radius: 8px;
    overflow: hidden;
    display: flex;
  }
  .legend-swatch { width: 34px; background: var(--legend-swatch); }
  .legend-text {
    flex: 1;
    background: var(--legend-body);
    color: var(--label);
    font-family: "Open Sans", Arial, sans-serif;
    font-size: 11px;
    line-height: 14px;
    padding: 6px 0 0 8px;
  }
</style>
</head>
<body>
<div class="canvas">
  <svg class="pyramid" viewBox="0 0 1200 1000" xmlns="http://www.w3.org/2000/svg" aria-hidden="true">
    <defs>
      <clipPath id="clip-email"><path d="M186 698 L583 82 Q601 58 619 82 L709 220 L398 698 Z"/></clipPath>
      <clipPath id="clip-presentations"><path d="M721 242 L1014 698 L800 698 L613 409 Z"/></clipPath>
    </defs>

    <!-- Email, nurture, print & social -->
    <g class="block">
      <g clip-path="url(#clip-email)">
        <rect x="150" y="40" width="600" height="700" fill="var(--blue)"/>
        <polygon points="150,698 580,40 660,40 640,117 254,698" fill="var(--blue-paywall)"/>
      </g>
    </g>

    <!-- Presentations & CMA -->
    <g class="block">
      <g clip-path="url(#clip-presentations)">
        <rect x="600" y="230" width="430" height="480" fill="var(--gold)"/>
        <polygon points="721,242 1030,242 1030,698 943,698 680,307" fill="var(--gold-paywall)"/>
      </g>
    </g>

    <!-- Contacts arrow -->
    <g class="block">
      <polygon points="599,430 774,698 665,698 665,814 535,814 535,698 425,698" fill="var(--navy)"/>
      <rect x="535" y="814" width="130" height="56" fill="var(--navy-paywall)"/>
    </g>

    <!-- Websites & leads -->
    <g class="block">
      <path d="M170 721 H512 V814 H112 Z" fill="var(--coral)"/>
      <path d="M112 814 H512 V870 H106 Q82 870 90 850 Q93 843 97 837 Z" fill="var(--coral-paywall)"/>
    </g>

    <!-- Mobile -->
    <g class="block">
      <path d="M688 721 H1030 L1089 814 H688 Z" fill="var(--teal)"/>
      <path d="M688 814 H1089 L1104 837 Q1118 862 1094 870 H688 Z" fill="var(--teal-paywall)"/>
    </g>

    <!-- Email / social hub icon -->
    <g class="icon" transform="translate(458 409)">
      <rect x="-29" y="-24" width="18" height="13" rx="1.5"/>
      <path d="M-29 -24 L-20 -17 L-11 -24 M-29 -11 L-22 -17 M-11 -11 L-18 -17"/>
      <rect x="11" y="-24" width="18" height="13" rx="1.5"/>
      <path class="solid" d="M17 -21 L23 -17.5 L17 -14 Z"/>
      <rect x="-29" y="11" width="18" height="13" rx="1.5"/>
      <circle cx="-20" cy="17.5" r="3.5"/>
      <rect x="11" y="11" width="18" height="13" rx="1.5"/>
      <path class="solid" d="M15 16 h3 v5 h-3 Z M19 14 h3 v7 h-3 Z M23 12.5 h3 v8.5 h-3 Z"/>
      <circle cx="0" cy="0" r="9"/>
      <path class="solid" d="M0 5 L-4.5 0 Q-6 -4 -2.5 -4.5 Q-1 -4.5 0 -2.5 Q1 -4.5 2.5 -4.5 Q6 -4 4.5 0 Z"/>
      <path d="M-11 -11 L-6.5 -6.5 M11 -11 L6.5 -6.5 M-11 11 L-6.5 6.5 M11 11 L6.5 6.5"/>
    </g>

    <!-- Presentation board icon -->
    <g class="icon" transform="translate(794 480)">
      <rect x="-22" y="-25" width="46" height="31" rx="2"/>
      <path d="M1 6 L1 10 M1 10 L-8 20 M1 10 L10 20"/>
      <rect x="-14" y="-10" width="5" height="11"/>
      <rect x="-5" y="-16" width="5" height="17"/>
      <rect x="4" y="-12" width="5" height="13"/>
      <rect x="13" y="-14" width="5" height="15"/>
    </g>

    <!-- Contact book icon -->
    <g class="icon" transform="translate(600 601)">
      <rect x="-21" y="-24" width="42" height="49" rx="3"/>
      <path d="M-14 -24 V25 M-21 -15 H-14 M-21 -6 H-14 M-21 3 H-14 M-21 12 H-14"/>
      <circle cx="4" cy="-9" r="5"/>
      <path d="M-7 5 Q-7 -3 4 -3 Q15 -3 15 5 Z"/>
      <path d="M-6 12 H15 M-6 17 H15"/>
    </g>

    <!-- Browser globe icon -->
    <g class="icon" transform="translate(224 800)">
      <rect x="-24" y="-24" width="48" height="46" rx="2"/>
      <path d="M-24 -15 H24"/>
      <circle class="solid" cx="-19" cy="-19.5" r="1.4"/>
      <circle class="solid" cx="-14.5" cy="-19.5" r="1.4"/>
      <circle class="solid" cx="-10" cy="-19.5" r="1.4"/>
      <path d="M9 -19.5 H20"/>
      <circle cx="0" cy="6" r="17"/>
      <ellipse cx="0" cy="6" rx="7" ry="17"/>
      <path d="M-17 6 H17 M-14 -3 H14 M-14 15 H14 M0 -11 V23"/>
    </g>

    <!-- Phone share icon -->
    <g class="icon" transform="translate(826 800)">
      <rect x="-22" y="-22" width="28" height="46" rx="4"/>
      <path d="M-11 -18 H-3 M-11 20 H-3 M-17 -13 H1 M-17 15 H1"/>
      <path d="M-15 -4 H-1 M-15 0 H-1 M-15 4 H-1 M-15 8 H-5"/>
      <circle cx="12" cy="-14" r="12" fill="var(--teal)"/>
      <circle cx="17" cy="-20" r="2.3"/>
      <circle cx="7" cy="-14" r="2.3"/>
      <circle cx="17" cy="-8" r="2.3"/>
      <path d="M9 -15 L15 -19 M9 -13 L15 -9"/>
    </g>
  </svg>

  <p class="module-label label-email">EMAIL, NURTURE<br>PRINT &amp; SOCIAL</p>
  <p class="module-label label-presentations">PRESENTATIONS<br>&amp; CMA</p>
  <p class="module-label label-contacts">CONTACTS</p>
  <p class="module-label label-websites">WEBSITES &amp; LEADS</p>
  <p class="module-label label-mobile">MOBILE</p>

  <div class="legend">
    <div class="legend-swatch"></div>
    <div class="legend-text">Lighter areas inciate<br>Paywall feature</div>
  </div>
</div>
</body>
</html>
```